Varlow Landscaping

Create a website for a new landscaping company. I have a logo already and description of services offered. I have a website that I would like all inquiries and appointments to get forwarded to. I need just need it well organized so that a husband and wife team can manage it easily. This is a company that will continue to grow over time and will need to add more services under new tabs over time. If you need the email where appointments and inquiries should go please send me a message.
Services offered are: Weekly/bi weekly mowing, weed eating and edging, Plant installation pinestraw & mulch installation, weed & feed, leaf removal and yard clean up.

```html
<!DOCTYPE html>
<html lang="en">
<head>
<meta charset="utf-8">
<title>Varlow Landscaping</title>
<link href="https://fonts.googleapis.com/css2?family=Poppins:wght@400;500;600;700&display=swap" rel="stylesheet">
<style>
:root{
  --green:#2d5b1c;
  --green-dark:#24491a;
  --gold:#e3a62a;
  --gold-soft:#f6e9c8;
  --cream:#fcf8ef;
  --ink:#1f1f1f;
  --text:#3d3d3d;
  --white:#ffffff;
  --line:#d9d9d9;
}
*{box-sizing:border-box;margin:0;padding:0}
html,body{width:1200px;height:4854px;overflow:hidden}
body{font-family:"Poppins",sans-serif;color:var(--text);background:var(--white);position:relative}
.abs{position:absolute}
section,header,footer{position:absolute;left:0;width:1200px}
.btn{position:absolute;display:flex;align-items:center;justify-content:center;background:var(--gold);color:var(--white);font-weight:600;font-size:13px;text-transform:uppercase;border-radius:30px;letter-spacing:.2px}
.btn-soft{background:var(--gold-soft);color:var(--gold)}
.heading{position:absolute;font-weight:600;text-transform:uppercase;color:var(--ink);font-size:38px;letter-spacing:.5px;line-height:1}
.heading.center{left:0;width:1200px;text-align:center}
.heading.light{color:var(--white)}
.heading u{text-decoration:none;border-bottom:3px solid var(--gold);padding-bottom:2px}
.social{position:absolute;width:30px;height:30px;border-radius:50%;background:var(--white);box-shadow:0 2px 6px rgba(0,0,0,.15)}
.social.active{background:var(--gold)}
.social::after{content:"";position:absolute;left:11px;top:11px;width:8px;height:8px;border-radius:2px;background:var(--gold)}
.social.active::after{background:var(--white)}
.wordmark{font-weight:700;color:var(--green);font-size:30px;letter-spacing:.5px}

/* header */
.site-header{top:0;height:140px;background:var(--white);z-index:3}
.nav-link{position:absolute;top:93px;font-size:14px;font-weight:500;color:var(--ink);text-transform:uppercase}
.nav-link.current{color:var(--gold);border-bottom:2px solid var(--gold);padding-bottom:2px}
.logo-badge{position:absolute;left:505px;top:0;width:190px;height:190px;border-radius:0 0 95px 95px;background:var(--white);display:flex;align-items:center;justify-content:center;z-index:4}
.logo-badge .dot{width:16px;height:16px;border-radius:50%;background:var(--gold);margin-right:8px}

/* hero */
.hero{top:0;height:790px}
.hero-photo{position:absolute;inset:0;background:linear-gradient(160deg,#4d6e2a 0%,#6e8f35 35%,#3e5e22 65%,#2f4d1b 100%)}
.hero-shade{position:absolute;inset:0;background:rgba(0,0,0,.22)}
.hero-title{position:absolute;top:300px;left:0;width:1200px;text-align:center;color:var(--white);font-weight:700;font-size:40px;line-height:48px;text-transform:uppercase}
.hero-sub{position:absolute;top:402px;left:250px;width:700px;text-align:center;color:var(--white);font-weight:600;font-size:19px;line-height:31px}
.hero-dots{position:absolute;left:1138px;top:394px}
.hero-dots span{display:block;width:12px;height:12px;border-radius:50%;border:2px solid var(--white);margin-bottom:11px}
.hero-dots span.on{background:var(--white)}
.wave{position:absolute;left:0;width:1200px}

/* about */
.about{top:790px;height:600px}
.about p{position:absolute;left:111px;width:464px;font-size:15px;line-height:26px;text-align:justify;color:var(--text)}
.blob{position:absolute;border-radius:50%}

/* services */
.services{top:1390px;height:580px;background:var(--cream)}
.service-card{position:absolute;top:155px;width:228px;height:350px;background:var(--white);border-radius:6px;box-shadow:0 4px 14px rgba(0,0,0,.1);text-align:center}
.service-icon{position:absolute;left:65px;top:24px;width:98px;height:98px;border-radius:50%;background:var(--green);border:3px solid var(--white);box-shadow:0 0 0 2px var(--green);display:flex;align-items:center;justify-content:center}
.service-icon.gold{background:var(--gold);box-shadow:0 0 0 2px var(--gold)}
.service-card h3{position:absolute;top:136px;left:10px;width:208px;font-size:16px;font-weight:600;line-height:26px;color:var(--ink);text-transform:uppercase}
.service-card p{position:absolute;top:192px;left:14px;width:200px;font-size:14px;line-height:24px;color:var(--text)}
.service-card .btn{left:38px;top:278px;width:152px;height:44px}
.chev{position:absolute;width:30px;height:30px}

/* why */
.why{top:1969px;height:660px;background:linear-gradient(180deg,var(--green) 0%,var(--green-dark) 100%)}
.why-icon{position:absolute;width:76px;height:76px;border-radius:50%;background:var(--white);border:4px solid rgba(255,255,255,.5);background-clip:padding-box;display:flex;align-items:center;justify-content:center}
.why-icon.gold{background:var(--gold)}
.why-label{position:absolute;color:var(--white);font-size:15px;font-weight:600;text-transform:uppercase;white-space:nowrap}

/* testimonials */
.testimonials{top:2629px;height:518px;background:var(--white)}
.review{position:absolute;top:131px;width:306px;height:278px;background:var(--white);border-top:4px solid var(--gold);border-radius:6px;box-shadow:0 4px 14px rgba(0,0,0,.1);text-align:center}
.avatar{position:absolute;left:106px;top:-80px;width:94px;height:94px;border-radius:50%;border:4px solid var(--gold);background:linear-gradient(135deg,#d8d8d8,#a9a9a9)}
.review h4{position:absolute;top:60px;left:0;width:100%;font-size:16px;font-weight:600;color:var(--ink);text-transform:uppercase}
.stars{position:absolute;top:88px;left:0;width:100%;color:var(--gold);font-size:13px;letter-spacing:2px}
.review p{position:absolute;top:110px;left:24px;width:258px;font-size:14px;line-height:23.5px;color:var(--text)}
.round-btn{position:absolute;width:34px;height:34px;border-radius:50%;display:flex;align-items:center;justify-content:center}

/* works */
.works{top:3147px;height:618px;background:var(--cream)}
.work-photo{position:absolute;top:163px;width:443px;height:294px;border-radius:0 30px 0 30px}
.side-tag{position:absolute;font-size:13px;font-weight:600;letter-spacing:2px;color:var(--green);transform:rotate(-90deg);transform-origin:left top}

/* contact */
.contact{top:3765px;height:800px;background:linear-gradient(180deg,var(--green) 0%,#2a5019 100%)}
.info{position:absolute;top:146px;color:var(--white);font-size:14px;line-height:18px}
.info b{font-weight:500;text-transform:uppercase;display:block}
.field-label{position:absolute;color:var(--white);font-size:15px;font-weight:500}
.field{position:absolute;background:var(--white);height:44px;width:435px;font-size:13px;font-style:italic;color:#9a9a9a;padding:13px 18px}

/* footer */
.site-footer{top:4560px;height:294px;background:var(--white)}
.foot-title{position:absolute;top:-6px;font-size:16px;font-weight:600;color:var(--green);text-transform:uppercase}
.foot-link{position:absolute;left:352px;font-size:14px;color:var(--text);display:flex;align-items:center}
.foot-link i{display:inline-block;width:12px;height:12px;border-radius:50%;background:var(--ink);margin-right:15px;position:relative}
.foot-link i::after{content:"";position:absolute;left:3px;top:4px;border:2px solid var(--white);border-width:0 2px 2px 0;width:3px;height:3px;transform:rotate(-45deg)}
.foot-info{position:absolute;left:567px;font-size:12px;line-height:20px;color:var(--text)}
.foot-info b{font-size:14px;font-weight:500;text-transform:uppercase;color:var(--ink);display:block}
</style>
</head>
<body>

<!-- HERO -->
<section class="hero">
  <div class="hero-photo" role="img" aria-label="Landscaper in work clothes mowing a lush garden lawn with a push mower"></div>
  <div class="hero-shade"></div>
  <h1 class="hero-title">Your Neighborhood<br>Lawn Experts</h1>
  <p class="hero-sub">Reliable mowing, landscaping, and seasonal yard care from a local family-owned team you can trust.</p>
  <div class="btn" style="left:463px;top:483px;width:274px;height:44px;font-size:14px">Schedule An Appointment</div>
  <div class="hero-dots"><span></span><span class="on"></span><span></span><span></span></div>
  <svg class="wave" style="top:640px" width="1200" height="150" viewBox="0 0 1200 150">
    <path d="M0 150 Q600 -10 1200 150 Z" fill="var(--gold)"/>
    <path d="M0 150 Q600 22 1200 150 Z" fill="var(--white)"/>
  </svg>
</section>

<!-- HEADER -->
<header class="site-header">
  <div class="abs" style="left:114px;top:22px;width:42px;height:42px;border-radius:50%;background:var(--white);box-shadow:0 2px 8px rgba(0,0,0,.15);display:flex;align-items:center;justify-content:center">
    <svg width="18" height="18" viewBox="0 0 24 24"><path d="M6.6 10.8a15 15 0 0 0 6.6 6.6l2.2-2.2c.3-.3.7-.4 1-.2 1.1.4 2.3.6 3.6.6.6 0 1 .4 1 1V20c0 .6-.4 1-1 1C10.6 21 3 13.4 3 4c0-.6.4-1 1-1h3.5c.6 0 1 .4 1 1 0 1.3.2 2.5.6 3.6.1.3 0 .7-.2 1z" fill="var(--gold)"/></svg>
  </div>
  <div class="abs" style="left:176px;top:22px;font-size:11px;font-weight:600;color:var(--ink)">CALL US:</div>
  <div class="abs" style="left:176px;top:40px;font-size:17px;font-weight:500;color:var(--ink)">+1 (555) 014 2736</div>
  <a class="nav-link current" style="left:110px">Home</a>
  <a class="nav-link" style="left:185px">About Us</a>
  <a class="nav-link" style="left:291px">Our Services</a>
  <a class="nav-link" style="left:770px">Projects</a>
  <a class="nav-link" style="left:878px">Contact</a>
  <div class="btn" style="left:942px;top:22px;width:147px;height:42px;font-size:13px">Get A Quote</div>
  <div class="social active" style="left:983px;top:87px" aria-label="Social profile"></div>
  <div class="social" style="left:1018px;top:87px" aria-label="Social profile"></div>
  <div class="social" style="left:1055px;top:87px" aria-label="Social profile"></div>
</header>
<div class="logo-badge"><span class="dot"></span><span class="wordmark">Varlow</span></div>

<!-- ABOUT -->
<section class="about">
  <h2 class="heading" style="left:111px;top:78px">About <u>Us</u></h2>
  <p style="top:148px">We’re a husband-and-wife team dedicated to keeping your property clean, healthy, and beautiful all year long. From weekly mowing to full yard cleanups and landscaping installs, we treat every lawn like it’s our own — with attention to detail and dependable service you can rely on.</p>
  <p style="top:312px">Lorem ipsum dolor sit amet, consectetur adipiscing elit, sed do eiusmod tempor incididunt ut labore et dolore magna aliqua ut enim ad minimea.</p>
  <div class="btn" style="left:113px;top:420px;width:153px;height:45px">Learn More</div>
  <div class="blob" style="left:935px;top:13px;width:190px;height:190px;background:#e4e7e1"></div>
  <div class="blob" style="left:637px;top:48px;width:452px;height:452px;border:4px solid var(--gold);background:linear-gradient(150deg,#7ea046,#3f6a26 60%,#5d8a34)" role="img" aria-label="Gardener trimming grass edges with a string trimmer"></div>
  <div class="blob" style="left:620px;top:308px;width:192px;height:192px;border:5px solid var(--white);background:linear-gradient(135deg,#6b8e3a,#4a3a2a 70%,#8a8a84)" role="img" aria-label="Gloved hands planting a fresh garden bed beside stone edging"></div>
</section>

<!-- SERVICES -->
<section class="services">
  <h2 class="heading center" style="top:76px">Our <u>Services</u></h2>
  <svg class="chev" style="left:36px;top:315px" viewBox="0 0 24 24"><path d="M15 4 7 12l8 8" fill="none" stroke="#9a9a9a" stroke-width="3"/></svg>
  <svg class="chev" style="left:1134px;top:315px" viewBox="0 0 24 24"><path d="M9 4l8 8-8 8" fill="none" stroke="var(--green)" stroke-width="3"/></svg>

  <div class="service-card" style="left:111px">
    <div class="service-icon"><svg width="46" height="46" viewBox="0 0 48 48" fill="none" stroke="#fff" stroke-width="2"><rect x="10" y="22" width="24" height="10" rx="2"/><circle cx="14" cy="36" r="4"/><circle cx="32" cy="36" r="4"/><path d="M34 22 42 8"/></svg></div>
    <h3>Weekly &amp; Bi-Weekly<br>Mowing</h3>
    <p>Consistent cuts to keep your lawn looking sharp and healthy.</p>
    <div class="btn btn-soft">Learn More</div>
  </div>
  <div class="service-card" style="left:361px">
    <div class="service-icon"><svg width="46" height="46" viewBox="0 0 48 48" fill="none" stroke="#fff" stroke-width="2"><path d="M34 6 18 34"/><circle cx="16" cy="37" r="4"/><path d="M8 42c2-6 4-6 6-4M26 42c0-5 3-7 5-6M38 42c-1-4 1-6 3-6"/></svg></div>
    <h3>Weed Eating &amp;<br>Edging</h3>
    <p>Clean lines around driveways, fences, and walkways.</p>
    <div class="btn btn-soft">Learn More</div>
  </div>
  <div class="service-card" style="left:611px">
    <div class="service-icon gold"><svg width="46" height="46" viewBox="0 0 48 48" fill="none" stroke="#fff" stroke-width="2"><path d="M24 28V14"/><path d="M24 20c-6 0-9-4-9-8 5 0 9 3 9 8zM24 18c0-5 4-8 9-8 0 5-4 8-9 8z"/><path d="M6 36h10l8-4h8c2 0 2 3 0 3h-8M16 40h14l12-8"/></svg></div>
    <h3>Plant<br>Installation</h3>
    <p>Flowers, shrubs, and plants to enhance curb appeal.</p>
    <div class="btn">Learn More</div>
  </div>
  <div class="service-card" style="left:861px">
    <div class="service-icon"><svg width="46" height="46" viewBox="0 0 48 48" fill="none" stroke="#fff" stroke-width="2"><path d="M14 30h20l-3 12H17z"/><path d="M24 30V12M24 24c-5-2-8-6-8-12 5 2 8 6 8 12zM24 24c5-2 8-6 8-12-5 2-8 6-8 12zM24 30c-6 0-10-4-12-8M24 30c6 0 10-4 12-8"/></svg></div>
    <h3>Pinestraw &amp;<br>Mulch Installation</h3>
    <p>Fresh beds that protect and beautify your landscape.</p>
    <div class="btn btn-soft">Learn More</div>
  </div>
</section>

<!-- WHY CHOOSE US -->
<section class="why">
  <h2 class="heading center light" style="top:73px">Why Choose Us</h2>
  <svg class="abs" style="left:0;top:0" width="1200" height="660" viewBox="0 0 1200 660">
    <path d="M325 560 A275 275 0 0 1 875 560" fill="none" stroke="#fff" stroke-width="2"/>
    <circle cx="599" cy="482" r="158" fill="none" stroke="#fff" stroke-width="2"/>
  </svg>
  <div class="abs" style="left:467px;top:350px;width:264px;height:264px;border-radius:50%;background:var(--white);display:flex;align-items:center;justify-content:center"><span class="wordmark">Varlow</span></div>
  <div class="why-label" style="left:0;width:1200px;text-align:center;top:160px">Honest Pricing</div>
  <div class="why-icon" style="left:561px;top:197px"><svg width="36" height="36" viewBox="0 0 24 24" fill="none" stroke="var(--gold)" stroke-width="1.5"><circle cx="14" cy="8" r="5"/><path d="M14 5v6M12.5 6.5h2.5a1 1 0 0 1 0 2h-2"/><path d="M3 20v-6h3l4 2h4"/></svg></div>
  <div class="why-label" style="right:833px;top:291px">Dependable Scheduling</div>
  <div class="why-icon" style="left:386px;top:262px"><svg width="36" height="36" viewBox="0 0 24 24" fill="none" stroke="var(--gold)" stroke-width="1.5"><rect x="3" y="5" width="16" height="15" rx="2"/><path d="M3 9h16M7 3v4M15 3v4"/><circle cx="18" cy="18" r="4" fill="#fff"/><path d="M16.5 18l1 1 2-2"/></svg></div>
  <div class="why-label" style="left:825px;top:289px">Attention To Detail</div>
  <div class="why-icon gold" style="left:727px;top:262px"><svg width="36" height="36" viewBox="0 0 24 24" fill="none" stroke="#fff" stroke-width="1.5"><path d="M5 3h10l3 3v8M5 3v18h9"/><path d="M8 8h6M8 11h6M8 14h3"/><circle cx="17" cy="17" r="3"/><path d="M19 19l3 3"/></svg></div>
  <div class="why-label" style="right:908px;top:434px">Family-Owned &amp; Local</div>
  <div class="why-icon" style="left:311px;top:405px"><svg width="36" height="36" viewBox="0 0 24 24" fill="none" stroke="var(--gold)" stroke-width="1.5"><circle cx="12" cy="12" r="8"/><circle cx="12" cy="10" r="2"/><circle cx="8" cy="13" r="1.5"/><circle cx="16" cy="13" r="1.5"/><path d="M9 17c0-2 6-2 6 0"/></svg></div>
  <div class="why-label" style="left:912px;top:434px">Easy Communication</div>
  <div class="why-icon" style="left:812px;top:405px"><svg width="36" height="36" viewBox="0 0 24 24" fill="none" stroke="var(--gold)" stroke-width="1.5"><path d="M3 6h12v8H8l-3 3v-3H3z"/><path d="M15 9h6v8h-2v3l-3-3h-5v-3"/><path d="M6 10h6"/></svg></div>
  <svg class="wave" style="top:510px" width="1200" height="150" viewBox="0 0 1200 150">
    <path d="M0 150 Q600 -10 1200 150 Z" fill="var(--gold)"/>
    <path d="M0 150 Q600 22 1200 150 Z" fill="var(--white)"/>
  </svg>
</section>

<!-- TESTIMONIALS -->
<section class="testimonials">
  <h2 class="heading center" style="top:12px">Testimonials</h2>
  <div class="round-btn" style="left:43px;top:252px;background:#f1f1f1"><svg width="14" height="14" viewBox="0 0 24 24"><path d="M15 4 7 12l8 8" fill="none" stroke="var(--ink)" stroke-width="3"/></svg></div>
  <div class="round-btn" style="left:1121px;top:252px;background:var(--gold)"><svg width="14" height="14" viewBox="0 0 24 24"><path d="M9 4l8 8-8 8" fill="none" stroke="#fff" stroke-width="3"/></svg></div>
  <div class="review" style="left:111px"><div class="avatar" role="img" aria-label="Customer portrait"></div><h4>Maren Holt</h4><div class="stars">★★★★★</div><p>Lorem ipsum dolor sit amet, consectetur adipiscing elit, sed do eiusmod tempor incididunt ut labore et dolore magna aliqua. Ut enim ad minim veniam, quis nostrud exercitatea.</p></div>
  <div class="review" style="left:447px"><div class="avatar" role="img" aria-label="Customer portrait"></div><h4>Maren Holt</h4><div class="stars">★★★★★</div><p>Lorem ipsum dolor sit amet, consectetur adipiscing elit, sed do eiusmod tempor incididunt ut labore et dolore magna aliqua. Ut enim ad minim veniam, quis nostrud exercitatea.</p></div>
  <div class="review" style="left:783px"><div class="avatar" role="img" aria-label="Customer portrait"></div><h4>Maren Holt</h4><div class="stars">★★★★★</div><p>Lorem ipsum dolor sit amet, consectetur adipiscing elit, sed do eiusmod tempor incididunt ut labore et dolore magna aliqua. Ut enim ad minim veniam, quis nostrud exercitatea.</p></div>
</section>

<!-- WORKS -->
<section class="works">
  <h2 class="heading center" style="top:74px">See Our <u>Works</u></h2>
  <div class="side-tag" style="left:108px;top:246px">BEFORE</div>
  <div class="side-tag" style="left:1074px;top:500px">AFTER</div>
  <svg class="abs" style="left:38px;top:296px" width="40" height="24" viewBox="0 0 40 24"><path d="M38 12H3M13 2 3 12l10 10" fill="none" stroke="#7a7a7a" stroke-width="2"/></svg>
  <svg class="abs" style="left:1122px;top:296px" width="40" height="24" viewBox="0 0 40 24"><path d="M2 12h35M27 2l10 10-10 10" fill="none" stroke="#7a7a7a" stroke-width="2"/></svg>
  <div class="work-photo" style="left:145px;background:linear-gradient(160deg,#8aa84a,#4e7a2c 55%,#6f9a3a)" role="img" aria-label="Before: worker mowing an overgrown lawn"></div>
  <div class="work-photo" style="left:612px;background:linear-gradient(160deg,#6d7a5a,#3c5a24 45%,#7fbf3c)" role="img" aria-label="After: fresh mulch bed with hostas beside a yellow wheelbarrow on a green lawn"></div>
  <div class="btn" style="left:497px;top:496px;width:206px;height:45px">View More Works</div>
</section>

<!-- CONTACT -->
<section class="contact">
  <div class="abs" style="inset:0;background:linear-gradient(180deg,rgba(0,0,0,0) 60%,rgba(0,0,0,.12))" role="img" aria-label="Dim photo of a mown lawn behind the form"></div>
  <h2 class="heading center light" style="top:75px">Get In <u>Touch</u></h2>
  <svg class="abs" style="left:192px;top:140px" width="40" height="44" viewBox="0 0 24 26" fill="none" stroke="var(--gold)" stroke-width="1.5"><path d="M12 22s7-7 7-12a7 7 0 0 0-14 0c0 5 7 12 7 12z"/><circle cx="12" cy="10" r="2.5"/><path d="M5 20H3l-1 4h20l-1-4h-2"/></svg>
  <div class="info" style="left:254px"><b>Location:</b>465, Lorum Ipsum Dolore Sed,<br>United States</div>
  <svg class="abs" style="left:492px;top:140px" width="40" height="40" viewBox="0 0 24 24" fill="none" stroke="var(--gold)" stroke-width="1.4"><path d="M6.6 10.8a15 15 0 0 0 6.6 6.6l2.2-2.2c.3-.3.7-.4 1-.2 1.1.4 2.3.6 3.6.6.6 0 1 .4 1 1V20c0 .6-.4 1-1 1C10.6 21 3 13.4 3 4c0-.6.4-1 1-1h3.5c.6 0 1 .4 1 1 0 1.3.2 2.5.6 3.6.1.3 0 .7-.2 1z"/><path d="M14 3a7 7 0 0 1 7 7M14 6a4 4 0 0 1 4 4"/></svg>
  <div class="info" style="left:556px;top:150px"><b>Phone:</b>+1 (555) 014 2736</div>
  <svg class="abs" style="left:716px;top:140px" width="44" height="40" viewBox="0 0 26 24" fill="none" stroke="var(--gold)" stroke-width="1.4"><rect x="1" y="6" width="7" height="16" rx="1"/><rect x="8" y="2" width="16" height="20" rx="1"/><path d="M11 6h10M11 10h10M11 14h10M11 18h10"/></svg>
  <div class="info" style="left:782px;top:150px"><b>Email:</b>info@varlowlandscaping.com</div>

  <div class="field-label" style="left:147px;top:212px">First Name:</div>
  <div class="field" style="left:147px;top:238px">Enter Your First Name</div>
  <div class="field-label" style="left:618px;top:212px">Last Name:</div>
  <div class="field" style="left:618px;top:238px">Enter Your Last Name</div>
  <div class="field-label" style="left:147px;top:305px">Phone:</div>
  <div class="field" style="left:147px;top:331px">Enter Phone Number</div>
  <div class="field-label" style="left:618px;top:305px">Email:</div>
  <div class="field" style="left:618px;top:331px">Enter Email Address</div>
  <div class="field-label" style="left:147px;top:398px">Message</div>
  <div class="field" style="left:147px;top:423px;width:906px;height:89px">Enter Comments</div>
  <div class="btn" style="left:511px;top:534px;width:179px;height:44px">Send Message</div>

  <svg class="wave" style="top:650px" width="1200" height="150" viewBox="0 0 1200 150">
    <path d="M0 150 Q600 -40 1200 150 Z" fill="var(--gold)"/>
    <path d="M0 150 Q600 -8 1200 150 Z" fill="var(--white)"/>
  </svg>
</section>

<!-- FOOTER -->
<footer class="site-footer">
  <div class="abs" style="left:110px;top:78px;display:flex;align-items:center"><span style="width:16px;height:16px;border-radius:50%;background:var(--gold);margin-right:8px"></span><span class="wordmark">Varlow</span></div>

  <div class="foot-title" style="left:347px">Quick Links</div>
  <div class="foot-link" style="top:31px"><i></i>Home</div>
  <div class="foot-link" style="top:69px"><i></i>About Us</div>
  <div class="foot-link" style="top:107px"><i></i>Our Services</div>
  <div class="foot-link" style="top:145px"><i></i>Projects</div>
  <div class="foot-link" style="top:183px"><i></i>Contact</div>

  <div class="foot-title" style="left:533px">Contact Info</div>
  <svg class="abs" style="left:533px;top:34px" width="12" height="14" viewBox="0 0 24 26"><path d="M12 24s8-8 8-13a8 8 0 0 0-16 0c0 5 8 13 8 13z" fill="var(--ink)"/></svg>
  <div class="foot-info" style="top:30px"><b>Address:</b>465, Lorum Ipsum Dolore,<br>United State</div>
  <svg class="abs" style="left:533px;top:112px" width="12" height="12" viewBox="0 0 24 24"><path d="M6.6 10.8a15 15 0 0 0 6.6 6.6l2.2-2.2c.3-.3.7-.4 1-.2 1.1.4 2.3.6 3.6.6.6 0 1 .4 1 1V20c0 .6-.4 1-1 1C10.6 21 3 13.4 3 4c0-.6.4-1 1-1h3.5c.6 0 1 .4 1 1 0 1.3.2 2.5.6 3.6.1.3 0 .7-.2 1z" fill="var(--ink)"/></svg>
  <div class="foot-info" style="top:108px"><b>Phone:</b>+1 (555) 014 2736</div>
  <svg class="abs" style="left:533px;top:169px" width="13" height="11" viewBox="0 0 24 18"><rect width="24" height="18" rx="2" fill="var(--ink)"/><path d="M1 2l11 8 11-8" fill="none" stroke="#fff" stroke-width="2"/></svg>
  <div class="foot-info" style="top:165px"><b>Email:</b>info@varlowlandscaping.com</div>

  <div class="foot-title" style="left:778px">Newsletter Signup</div>
  <div class="abs" style="left:778px;top:32px;width:311px;height:45px;border-radius:30px;background:var(--white);box-shadow:0 2px 8px rgba(0,0,0,.15);font-size:13px;color:#6a6a6a;padding:13px 18px">Email Address</div>
  <div class="btn" style="left:982px;top:32px;width:107px;height:45px;font-size:12px">Sign Up</div>

  <div class="abs" style="left:111px;top:216px;width:978px;height:1px;background:var(--line)"></div>
  <div class="abs" style="left:0;top:234px;width:1200px;text-align:center;font-size:13px;color:var(--ink)">© 2026 Varlow Landscaping &nbsp;-&nbsp; All Rights Reserved</div>
  <div class="social active" style="left:963px;top:227px" aria-label="Social profile"></div>
  <div class="social" style="left:1008px;top:227px" aria-label="Social profile"></div>
  <div class="social" style="left:1051px;top:227px" aria-label="Social profile"></div>
</footer>

</body>
</html>
```